Business Card for a Dental Office

The design should communicate integrity, quality and reliability. We also want the card look elegant, simple, but still stand out, different from the traditional-dental-office business card.

Industry/Entity Type

Business

```html
<!DOCTYPE html>
<html lang="en">
<head>
<meta charset="utf-8">
<title>Larkfield Dental Studio – Business Card</title>
<link href="https://fonts.googleapis.com/css2?family=Open+Sans:wght@400;600;700&display=swap" rel="stylesheet">
<style>
  :root {
    --backdrop: #3b3b3d;
    --card: #ffffff;
    --gold: #b08d2a;
    --ink: #1c1c1c;
    --text: #333333;
    --rule: #9a9a9a;
  }
  * { box-sizing: border-box; margin: 0; padding: 0; }
  html, body {
    width: 1200px; height: 977px; overflow: hidden;
    background: var(--backdrop);
    font-family: "Open Sans", Arial, sans-serif;
  }
  .card {
    position: absolute; left: 100px; top: 203px;
    width: 1000px; height: 571px;
    background: var(--card);
    overflow: hidden;
  }
  .contact { position: absolute; left: 165px; top: 165px; }
  .contact__name {
    color: var(--gold); font-size: 34px; font-weight: 600; line-height: 1.1;
  }
  .contact__role {
    color: var(--ink); font-size: 17px; font-weight: 700; margin: 4px 0 0 10px;
  }
  .contact__list { list-style: none; margin: 28px 0 0 34px; }
  .contact__item {
    display: flex; align-items: flex-start; gap: 18px;
    color: var(--text); font-size: 19px; line-height: 1.55;
  }
  .contact__item + .contact__item { margin-top: 10px; }
  .contact__item--tight { margin-top: 2px !important; }
  .contact__icon { width: 20px; height: 20px; flex: none; margin-top: 6px; fill: var(--gold); }
  .divider { position: absolute; left: 440px; top: 115px; width: 60px; height: 290px; }
  .brand {
    position: absolute; left: 560px; top: 200px;
    display: flex; align-items: center; gap: 14px;
  }
  .brand__mark { width: 34px; height: 34px; background: var(--gold); }
  .brand__name {
    color: var(--ink); font-size: 30px; font-weight: 700; letter-spacing: 0.5px;
  }
  .band { position: absolute; right: 0; bottom: 0; width: 420px; height: 62px; }
  .band__url {
    position: absolute; right: 38px; bottom: 16px;
    color: #ffffff; font-size: 20px; font-weight: 400;
  }
</style>
</head>
<body>
  <section class="card">
    <div class="contact">
      <h1 class="contact__name">Owen Hartley</h1>
      <p class="contact__role">Manager</p>
      <ul class="contact__list">
        <li class="contact__item">
          <svg class="contact__icon" viewBox="0 0 20 20" aria-hidden="true"><path d="M10 1a6.5 6.5 0 0 0-6.5 6.5C3.5 12.5 10 19 10 19s6.5-6.5 6.5-11.5A6.5 6.5 0 0 0 10 1zm0 9a2.6 2.6 0 1 1 0-5.2A2.6 2.6 0 0 1 10 10z"/></svg>
          <span>5678 Harbor Lane,<br>CA 94107</span>
        </li>
        <li class="contact__item">
          <svg class="contact__icon" viewBox="0 0 20 20" aria-hidden="true"><path d="M4.2 1.5l3 3.4-1.7 2.4c1.2 2.7 3.3 4.8 6.1 6.1l2.4-1.7 3.4 3-1.6 3c-7.5-.6-13.6-6.6-14.3-14.3z"/></svg>
          <span>(800) 555-0142</span>
        </li>
        <li class="contact__item contact__item--tight">
          <svg class="contact__icon" viewBox="0 0 20 20" aria-hidden="true"><path d="M1 4h18v2.2l-9 5.5-9-5.5z"/><path d="M1 8.5l9 5.5 9-5.5V16H1z"/></svg>
          <span>hello@larkfielddental.com</span>
        </li>
      </ul>
    </div>

    <svg class="divider" viewBox="0 0 60 290" aria-hidden="true">
      <defs>
        <linearGradient id="ruleFade" x1="0" y1="0" x2="0" y2="1">
          <stop offset="0" stop-color="#9a9a9a" stop-opacity="0.2"/>
          <stop offset="0.5" stop-color="#9a9a9a" stop-opacity="1"/>
          <stop offset="1" stop-color="#9a9a9a" stop-opacity="0.2"/>
        </linearGradient>
      </defs>
      <line x1="5" y1="0" x2="55" y2="290" stroke="url(#ruleFade)" stroke-width="2"/>
    </svg>

    <div class="brand">
      <span class="brand__mark"></span>
      <span class="brand__name">LARKFIELD DENTAL STUDIO</span>
    </div>

    <svg class="band" viewBox="0 0 420 62" preserveAspectRatio="none" aria-hidden="true">
      <path d="M42 0 H420 V62 H0 C18 52 28 30 42 0 Z" fill="var(--gold)"/>
    </svg>
    <span class="band__url">www.larkfielddental.com</span>
  </section>
</body>
</html>
```